Veranaxis Business Card and Letter Head

We are a leadership assessment consultancy based in Carrowmere, Australia. We help executive-level decison-makers select leaders for more senior level roles in corporate and government organisations. Our methodology is based on the latest research from the field of neuroscience.
We need a business card design and matching letter head that presents our company, Veranaxis, as a:
1. trusted adviser to senior executive-level decison makers
2. niche consultancy who are experts in the field of assessing leadership talent
3. results-focused solution provider who balance scientific methods with pragmatic solutions
The following company details should be used in all designs:
Company Name: Veranaxis
Details (for business card):
Daniel Prescott
High Potential Officer
Level 18, Brenning Tower
7 Brenning Square
Carrowmere, NSW 2147 Australia
Phone: 1300 482 716
Mobile: 0412 573 208
Email: daniel.prescott@veranaxis.com.au
Website: veranaxis.com.au
I have attached the logo for Veranaxis (for both a white and black background) - your business card and letter head designs must incoporate this logo and colour scheme.
Thanks for your interest in this project, I'm looking forward to receiving your ideas.
Regards,
Daniel
Executive-level decison-makers in corporate and government organisations (e.g., CEO, VP, Head of Human Resources)
Leadership

```html
<!DOCTYPE html>
<html lang="en">
<head>
<meta charset="utf-8">
<title>Veranaxis Letterhead</title>
<link rel="stylesheet" href="https://fonts.googleapis.com/css2?family=Inter:wght@300;400;700&display=swap">
<style>
  :root {
    --ink: #231f20;
    --red: #b8261c;
    --black: #000000;
    --paper: #ffffff;
    --muted: #3c3c3c;
    --footer-text: #e2e2e2;
  }
  * { margin: 0; padding: 0; box-sizing: border-box; }
  html, body {
    width: 848px;
    height: 1200px;
    overflow: hidden;
    background: var(--paper);
  }
  .letterhead {
    position: relative;
    width: 848px;
    height: 1200px;
    background: var(--paper);
    font-family: "Inter", "Helvetica Neue", Arial, sans-serif;
  }
  .brand {
    position: absolute;
    left: 57px;
    top: 60px;
  }
  .brand-row {
    display: flex;
    align-items: center;
    gap: 16px;
  }
  .brand-square {
    width: 42px;
    height: 42px;
    background: var(--red);
  }
  .brand-name {
    font-weight: 700;
    font-size: 46px;
    line-height: 1;
    letter-spacing: -1.2px;
    color: var(--ink);
  }
  .brand-tagline {
    margin-top: 8px;
    margin-left: 58px;
    font-weight: 300;
    font-size: 12.5px;
    line-height: 1;
    letter-spacing: 0.2px;
    color: var(--muted);
    white-space: nowrap;
  }
  .corner-block {
    position: absolute;
    top: 0;
    right: 0;
    width: 140px;
    height: 139px;
    background: var(--red);
  }
  .footer {
    position: absolute;
    left: 0;
    bottom: 0;
    width: 848px;
    height: 54px;
  }
  .footer-band {
    position: absolute;
    left: 0;
    top: 0;
    width: 749px;
    height: 54px;
    background: var(--black);
    color: var(--footer-text);
    font-weight: 300;
    font-size: 11px;
    line-height: 15px;
    letter-spacing: -0.15px;
    white-space: nowrap;
  }
  .footer-address {
    position: absolute;
    left: 57px;
    top: 11px;
  }
  .footer-contact {
    position: absolute;
    right: 12px;
    top: 11px;
    text-align: right;
  }
  .footer-accent {
    position: absolute;
    right: 0;
    top: 0;
    width: 92px;
    height: 54px;
    background: var(--red);
  }
</style>
</head>
<body>
  <main class="letterhead">
    <header class="brand">
      <div class="brand-row">
        <div class="brand-square"></div>
        <div class="brand-name">Veranaxis</div>
      </div>
      <div class="brand-tagline">ASSESSING EXECUTIVE CAPABILITY</div>
    </header>

    <div class="corner-block"></div>

    <footer class="footer">
      <div class="footer-band">
        <div class="footer-address">
          Level 18, Brenning Tower, 7 Brenning Square, Carrowmere, NSW 2147 Australia<br>
          Phone: 1300 482 716&nbsp; Mobile: 0412 573 208
        </div>
        <div class="footer-contact">
          Email: daniel.prescott@veranaxis.com.au<br>
          Website: veranaxis.com.au
        </div>
      </div>
      <div class="footer-accent"></div>
    </footer>
  </main>
</body>
</html>
```